Sports & fitness accessories website needs web design

We have a prestashop website that needs an appropriate skin that will work on the site and translate onto amazon and ebay shops.
The site is currently live www.strongpeak.co.uk
Target Market(s)
Sports & fitness enthusiasts
Industry/Entity Type
Fitness
Number of Pages Required
5+ page
Font styles to use
Sans Serif

```html
<!DOCTYPE html>
<html lang="en">
<head>
<meta charset="utf-8">
<title>StrongPeak – Reach Your Peak</title>
<link href="https://fonts.googleapis.com/css2?family=Lato:wght@400;700&family=Saira+Semi+Condensed:wght@500;600&display=swap" rel="stylesheet">
<style>
:root{
  --orange:#f7931e;
  --orange-dark:#e07a0c;
  --black:#0b0b0b;
  --panel:#3a3a3a;
  --panel-dark:#2b2b2b;
  --sidebar:#4a4a4a;
  --text-light:#e6e6e6;
  --muted:#9a9a9a;
  --footer-bg:#e9e9e9;
  --footer-bar:#d6d6d6;
}
*{box-sizing:border-box;margin:0;padding:0}
html,body{width:743px;height:1200px;overflow:hidden}
body{background:var(--black);font-family:'Lato',sans-serif;color:var(--text-light);position:relative}
.abs{position:absolute}
a{color:inherit;text-decoration:none}

/* header */
.topbar{top:5px;right:77px;font-size:8px;color:#ddd;display:flex}
.topbar span{padding:0 6px;border-left:1px solid #555}
.topbar span:first-child{border:none;display:flex;align-items:center;gap:3px}
.brand{left:77px;top:10px;width:110px}
.brand-name{font-weight:700;font-size:17px;color:var(--orange)}
.brand-tag{font-size:6.5px;color:#ccc;margin-top:3px;letter-spacing:.2px;white-space:nowrap}
.shipping{top:35px;left:377px;font-size:7px;color:#fff;font-weight:700;white-space:nowrap}
.shipping em{font-style:normal;font-weight:400;color:#ccc}
.cart{left:576px;top:31px;width:90px;height:19px;background:var(--orange);border-radius:10px;font-size:7px;color:#fff;display:flex;align-items:center;padding-left:4px;gap:4px;white-space:nowrap}
.cart b{width:12px;height:12px;border-radius:50%;background:#fff;display:flex;align-items:center;justify-content:center}
.nav{left:76px;top:70px;display:flex;align-items:center;gap:13px;font-size:8px;font-weight:700;color:#fff;white-space:nowrap}
.search{left:545px;top:68px;width:121px;height:14px;background:#fff;font-size:7.5px;color:#999;padding:2px 9px}
.search svg{position:absolute;right:4px;top:2px}
.rule{left:0;top:87px;width:743px;border-top:1px dashed var(--orange)}

/* slider */
.hero{left:76px;top:105px;width:590px;height:225px;background:linear-gradient(160deg,#5a5a5a 0%,#2a2a2a 40%,#1a1a1a 60%,#6b6b6b 100%);overflow:hidden}
.hero-arrow{top:94px;width:22px;height:36px;background:rgba(255,255,255,.85);display:flex;align-items:center;justify-content:center}
.hero-caption{left:15px;top:196px;font-family:'Saira Semi Condensed',sans-serif;font-weight:500;font-size:19px;line-height:22px;color:#fff;white-space:nowrap}

/* promos */
.promo{top:343px;height:111px;background:var(--orange);overflow:hidden}
.promo-art{position:absolute;left:10px;top:10px;width:120px;height:90px;background:radial-gradient(circle at 40% 50%,#fff4 0,#e9780a 70%)}
.promo h2{position:absolute;right:16px;font-family:'Saira Semi Condensed',sans-serif;font-weight:600;color:#fff;font-size:19px;text-align:right;line-height:24px;letter-spacing:.5px;white-space:nowrap}
.promo .btn{position:absolute;right:13px;bottom:11px;background:#fff;color:#222;font-size:8.5px;font-weight:700;padding:4px 10px}

/* tabs */
.tabs{left:76px;top:480px;width:590px;height:348px;background:var(--panel)}
.tab{position:absolute;top:0;height:30px;display:flex;align-items:center;justify-content:center;font-size:9px;font-weight:700;color:var(--orange);border-bottom:1px dashed #777}
.sidebar{position:absolute;left:0;top:30px;width:148px;height:318px;background:var(--sidebar)}
.sidebar ul{list-style:none;margin:13px 0 0 20px;font-size:9px;color:#ddd}
.sidebar li{height:19.2px}
.side-promo{position:absolute;left:19px;top:189px;width:109px;height:115px;background:linear-gradient(180deg,#c9c9c9,#8a8a8a)}
.side-promo .lbl{position:absolute;right:12px;top:44px;font-size:10px;color:#fff}
.side-promo .pct{position:absolute;left:12px;top:56px;font-size:17px;font-weight:700;color:#fff;white-space:nowrap}
.side-promo .pct b{font-size:28px}
.side-promo .buy{position:absolute;right:8px;bottom:6px;background:var(--orange);color:#fff;font-size:8px;padding:3px 9px}
.product{position:absolute;width:110px;font-size:6.5px;color:#ddd;line-height:8.5px;white-space:nowrap}
.product .img{width:89px;height:89px;background:#fff;position:relative;overflow:hidden;margin-bottom:8px}
.product .img div{position:absolute;inset:14px;border-radius:6px}
.product .img .tag{position:absolute;right:0;bottom:0;width:0;height:0;border-left:30px solid transparent;border-bottom:30px solid var(--orange)}
.product .row{position:absolute;left:0;display:flex;gap:20px;color:var(--orange)}
.pager{position:absolute;left:148px;top:328px;width:442px;height:20px;background:var(--orange);display:flex;align-items:center;justify-content:center;gap:6px;font-size:11px;color:#fff}
.pager .on{background:#eee;color:#333;width:20px;height:20px;display:flex;align-items:center;justify-content:center}

/* features */
.feature{top:858px;width:170px;text-align:center;margin-left:-85px}
.feature .ring{width:68px;height:68px;border-radius:50%;background:var(--orange);border:3px solid #9a5a10;margin:0 auto 16px;display:flex;align-items:center;justify-content:center}
.feature h3{font-size:11.5px;font-weight:700;color:#fff;margin-bottom:9px}
.feature p{font-size:8px;color:#ddd;line-height:11px}

/* footer */
.footer{left:76px;top:1014px;width:590px;height:186px;background:var(--footer-bg);color:#888}
.fcol{position:absolute;top:14px;font-size:7px;line-height:11.6px;color:#aaa;white-space:nowrap}
.fcol h4{font-size:8.5px;color:#666;font-weight:700;margin-bottom:4px}
.fsep{position:absolute;top:12px;height:140px;border-left:1px dashed #aaa}
.newsletter{position:absolute;left:405px;top:14px;width:160px}
.newsletter h4{font-size:8.5px;color:#666;margin-bottom:5px}
.nl-box{background:#bcbcbc;padding:5px;height:27px;display:flex;gap:4px}
.nl-box span{flex:1;background:#fff;font-size:6.5px;color:#aaa;padding:3px 5px}
.nl-box b{width:22px;background:#fff}
.nl-note{font-size:6px;font-style:italic;color:#888;margin:4px 0 9px 6px}
.socials{display:flex;gap:5px;margin-left:5px}
.socials i{width:20px;height:20px;border-radius:50%;display:block}
.pay{display:flex;gap:3px;margin-top:6px;background:#ddd;padding:3px}
.pay i{width:22px;height:14px;display:block;border-radius:2px}
.fbar{position:absolute;left:0;bottom:0;width:590px;height:24px;background:var(--footer-bar);font-size:7px;color:#444;display:flex;align-items:center;justify-content:center}
</style>
</head>
<body>

<header>
  <div class="abs topbar">
    <span><svg width="8" height="8" viewBox="0 0 24 24"><path fill="#fff" d="M6.6 10.8a15 15 0 006.6 6.6l2.2-2.2c.3-.3.7-.4 1-.2 1.1.4 2.3.6 3.6.6.6 0 1 .4 1 1V20c0 .6-.4 1-1 1A17 17 0 013 4c0-.6.4-1 1-1h3.5c.6 0 1 .4 1 1 0 1.3.2 2.5.6 3.6.1.3 0 .7-.2 1z"/></svg>07700 900 418</span>
    <span>Contact Us</span><span>English</span><span>Currency: GBP</span><span>Sign in</span>
  </div>
  <div class="abs brand">
    <div class="brand-name">StrongPeak</div>
    <div class="brand-tag">Reach Your Peak</div>
  </div>
  <div class="abs shipping">FREE SHIPPING, HOME TRY-ONS &amp; RETURNS <em>see details</em></div>
  <div class="abs cart"><b><svg width="7" height="7" viewBox="0 0 24 24"><path fill="#f7931e" d="M3 4h3l3 11h10l2-8H7"/></svg></b>Cart: 0 item(s) - $0.00</div>
  <nav class="abs nav">
    <svg width="11" height="10" viewBox="0 0 24 22"><path fill="#f7931e" d="M12 1L1 11h3v10h6v-6h4v6h6V11h3z"/></svg>
    <a>Gym Accessories</a><a>Fitness Accessories</a><a>Weights</a><a>Yoga</a><a>Swimming</a><a>Training</a><a>Footwear</a><a>Sale</a>
  </nav>
  <div class="abs search">Search<svg width="10" height="10" viewBox="0 0 24 24"><circle cx="10" cy="10" r="6" stroke="#888" stroke-width="2.5" fill="none"/><path d="M15 15l6 6" stroke="#888" stroke-width="3"/></svg></div>
  <div class="abs rule"></div>
</header>

<section class="abs hero" role="img" aria-label="Rack of black dumbbells with red end caps in a gym">
  <div class="abs hero-arrow" style="left:0;border-radius:0 18px 18px 0"></div>
  <div class="abs hero-arrow" style="right:0;border-radius:18px 0 0 18px"><svg width="8" height="12" viewBox="0 0 8 12"><path d="M1 1l5 5-5 5" stroke="#222" stroke-width="2" fill="none"/></svg></div>
  <p class="abs hero-caption">Lorem ipsum dolor sit amet, consectetuer adipiscing elit sed</p>
</section>

<section class="abs promo" style="left:80px;width:280px">
  <div class="promo-art" role="img" aria-label="Gift box and light bulb illustration"></div>
  <h2 style="top:10px">GIFT IDEA</h2>
  <a class="btn">Find Out More</a>
</section>
<section class="abs promo" style="left:384px;width:280px">
  <div class="promo-art" role="img" aria-label="Wrapped gift boxes illustration"></div>
  <h2 style="top:11px">SHOWCASE OF<br>PRODUCTS</h2>
  <a class="btn">Find Out More</a>
</section>

<section class="abs tabs">
  <div class="tab" style="left:0;width:148px;background:var(--sidebar)">CATEGORIES</div>
  <div class="tab" style="left:148px;width:216px;background:var(--panel)">POPULAR</div>
  <div class="tab" style="left:364px;width:226px;background:var(--panel-dark)">BEST SELLERS</div>
  <aside class="sidebar">
    <ul><li>Gym Accessories</li><li>Fitness Accessories</li><li>Weights</li><li>Yoga</li><li>Swimming</li><li>Training</li><li>Footwear</li><li>Sale</li></ul>
    <div class="side-promo" role="img" aria-label="Runner's legs in trainers">
      <span class="lbl">Footwear</span>
      <span class="pct"><b>20</b>% Off</span>
      <span class="buy">Buy Now</span>
    </div>
  </aside>

  <div class="product" style="left:185px;top:42px"><div class="img"><div role="img" aria-label="Black flex bench" style="background:#2a2a2a;inset:20px 14px"></div></div>Ridgeline Fitness Accessories<br>Training Series Flex Bench<div class="row" style="top:115px"><span>£299.99</span><span>Add to Cart</span></div></div>
  <div class="product" style="left:317px;top:42px"><div class="img"><div role="img" aria-label="Door sit up bar" style="background:#333;inset:22px 16px"></div><i class="tag"></i></div>Sit Up Bar<div class="row" style="top:115px"><span>£7.99</span><span>Add to Cart</span></div></div>
  <div class="product" style="left:447px;top:42px"><div class="img"><div role="img" aria-label="Pair of green hex dumbbells" style="background:#b7d51e"></div></div>2kg Neo-Hex<br>Dumbbell (Pair)<div class="row" style="top:115px"><span>£19.99</span><span>Add to Cart</span></div></div>

  <div class="product" style="left:185px;top:181px"><div class="img"><div role="img" aria-label="Blue and orange swim float board" style="background:linear-gradient(#2f6fc0,#f08a1c)"></div></div>Wavecrest Board<div class="row" style="top:115px"><span>£19.99</span><span>Add to Cart</span></div></div>
  <div class="product" style="left:317px;top:181px"><div class="img"><div role="img" aria-label="Red leather punch bag" style="background:#c0141b;inset:14px 38px"></div></div>Vantor Leather Punch<br>Bag 4ft - 25kg<div class="row" style="top:115px"><span>£149.99</span><span>Add to Cart</span></div></div>
  <div class="product" style="left:447px;top:181px"><div class="img"><div role="img" aria-label="Violet exercise mat" style="background:#8a63c4;inset:26px 12px"></div><i class="tag"></i></div>Cloudmat Studio Aerobic<br>Mat Violet Sml 14mm<div class="row" style="top:115px"><span>£12.99</span><span>Add to Cart</span></div></div>

  <div class="pager">
    <svg width="8" height="10"><path d="M7 0v10L0 5z" fill="#fff"/></svg>
    <span class="on">1</span><span>2</span><span>3</span><span>4</span>
    <svg width="8" height="10"><path d="M1 0v10l7-5z" fill="#fff"/></svg>
  </div>
</section>

<section class="abs feature" style="left:193px">
  <div class="ring"><svg width="30" height="22" viewBox="0 0 30 22"><path d="M1 2h17v14H1zM18 7h6l5 5v4H18z" fill="#111"/><circle cx="7" cy="18" r="3" fill="#111"/><circle cx="23" cy="18" r="3" fill="#111"/></svg></div>
  <h3>Delivery</h3>
  <p>We display orders world<br>wide from our state of the art<br>UK distribution centre</p>
</section>
<section class="abs feature" style="left:370px">
  <div class="ring"><svg width="26" height="26" viewBox="0 0 24 24"><path fill="#111" d="M6.6 10.8a15 15 0 006.6 6.6l2.2-2.2c.3-.3.7-.4 1-.2 1.1.4 2.3.6 3.6.6.6 0 1 .4 1 1V20c0 .6-.4 1-1 1A17 17 0 013 4c0-.6.4-1 1-1h3.5c.6 0 1 .4 1 1 0 1.3.2 2.5.6 3.6.1.3 0 .7-.2 1z"/></svg></div>
  <h3>Call Us</h3>
  <p>You can call us on<br>+44 7700 900 418</p>
</section>
<section class="abs feature" style="left:549px">
  <div class="ring"><svg width="30" height="22" viewBox="0 0 30 22"><rect x="2" y="2" width="26" height="18" rx="3" fill="none" stroke="#111" stroke-width="3"/><rect x="2" y="7" width="26" height="4" fill="#111"/></svg></div>
  <h3>Secure Payments</h3>
  <p>Payment can be made by<br>Debit or Crads &amp; payple</p>
</section>

<footer class="abs footer">
  <div class="fcol" style="left:30px"><h4>Categories</h4>Women<br>Yoga<br>Endurance<br>Gym Accessories<br>Weifhts<br>Swimming<br>Traning<br>Footwear<br>Clearance<br>Sale</div>
  <div class="fsep" style="left:120px"></div>
  <div class="fcol" style="left:150px"><h4>Information</h4>Specials<br>New Products<br>Best Sellers<br>Contact Us<br>Delivery<br>Legal Notice<br>Terms And Conditions<br>Privacy Policy<br>Returns<br>Sitemap</div>
  <div class="fsep" style="left:256px"></div>
  <div class="fcol" style="left:286px"><h4>My account</h4>My Orders<br>My Credit Slips<br>My Addresses<br>My Personal Info</div>
  <div class="fsep" style="left:375px"></div>
  <div class="newsletter">
    <h4>Sign Up For Our Newsletter</h4>
    <div class="nl-box"><span>your email...</span><b></b></div>
    <p class="nl-note">'Leave your email to subscribe'</p>
    <div class="socials"><i style="background:#2aa9e0"></i><i style="background:#3b5998"></i><i style="background:#444"></i><i style="background:#f39c12"></i><i style="background:#cb2027"></i><i style="background:#c0392b"></i></div>
    <h4 style="margin-top:12px;margin-bottom:0">SECURE PAYMENT</h4>
    <div class="pay"><i style="background:#c0392b"></i><i style="background:#1f5fa8"></i><i style="background:#eee"></i><i style="background:#1a3a8a"></i><i style="background:#4a8fd0"></i><i style="background:#eee"></i></div>
  </div>
  <div class="fbar">© 2015 StrongPeak. | Allrights Reserved</div>
</footer>

</body>
</html>
```